Private Gym Needs a Rack Card Design

We need a basic front and back rack card (same size as post card) that gives basic information about our brand, and includes our logo. Please see attached logo and required content below.

Target Market(s)

Upscale, private gym.

Industry/Entity Type

Gym

Font styles to use
Sans Serif

Colors
ffffff
5c5c5c
000000
dbdbdb
f78f20

Requirements
Must have
• Business Logo and the following text in a clean, modern, easy-to-read, artistic manner. Style and design must be clean, incorporate our color scheme of MOSTLY white, light grey, charcoal, with just pops of orange. We want the card itself to be mostly white background. Must include website URL as well: corevantagestudio.com
• FRONT CARD:
• Logo
• A safe and individualized approach to exercise
• Our method employs the latest weight resistance training exercises and coaching for healthy living. Not only is our workout methodology effective, it’s safe.
• Our Method…
• -Improves Functional Movement
• -Promotes Weight Loss
• -Builds Strength
• -Increases Flexibility 

• BACK:
• Change Your Body. Find Your Strength.
• There’s 40 years of success behind our proven method
• What is The Formwell? 
• The Formwell is all about teaching our clients how to lift weights and exercise with the proper technique. There’s no slinging or jerking at our gym; only controlled movements that yield real results.
• Come workout with us in our private gym. We are located in Durham adjacent to Harlow Campus and 5 minutes from downtown Durham.
• Address: 482 Linden Ave, Durham, NC 27705
• Phone: (919) 555-2741
• Hours: 9:00 AM – 9:00 PM
Nice to have
• Great organization of text, maybe some columns, colored bullet points, cool graphics and logos.
Should not have
• Busy or crowded design. All lines should be sleek, straight, and streamline. NO STOCK IMAGES, but logos are GREAT

```html
<!DOCTYPE html>
<html lang="en">
<head>
<meta charset="utf-8">
<title>The Formwell – Rack Card</title>
<link rel="stylesheet" href="https://fonts.googleapis.com/css2?family=Open+Sans:wght@400;600;700&display=swap">
<style>
  :root {
    --orange: #f0643a;
    --charcoal: #58595b;
    --light-grey: #dcdcdc;
    --pale-grey: #e9e9e9;
    --paper: #f6f6f6;
    --canvas: #d6d6d6;
    --text: #4a4a4a;
    --white: #ffffff;
  }
  * { box-sizing: border-box; margin: 0; padding: 0; }
  html, body { width: 1200px; height: 1000px; overflow: hidden; }
  body {
    background: var(--canvas);
    font-family: "Open Sans", Arial, sans-serif;
    color: var(--text);
    position: relative;
  }
  .card {
    position: absolute;
    left: 280px;
    width: 640px;
    height: 470px;
    background: var(--paper);
    overflow: hidden;
    box-shadow: 0 4px 14px rgba(0,0,0,0.18);
  }
  .card--front { top: 20px; }
  .card--back { top: 510px; }
  .card__stripes { position: absolute; inset: 0; width: 640px; height: 470px; }

  .brand {
    position: absolute;
    display: flex;
    align-items: center;
    gap: 10px;
  }
  .brand__mark { width: 16px; height: 16px; background: var(--orange); }
  .brand__name {
    font-size: 32px;
    font-weight: 700;
    color: var(--charcoal);
    letter-spacing: 1px;
    line-height: 1;
  }
  .card--front .brand { left: 320px; top: 62px; }
  .card--back .brand { left: 118px; top: 62px; }

  /* Front */
  .tagline-band {
    position: absolute;
    left: 105px; top: 175px;
    width: 530px; height: 34px;
    background: var(--orange);
    clip-path: polygon(0 0, 100% 0, 94% 100%, 0 100%);
    color: var(--white);
    font-weight: 700;
    font-size: 17px;
    letter-spacing: 0.6px;
    line-height: 34px;
    padding-left: 22px;
    white-space: nowrap;
  }
  .intro {
    position: absolute;
    left: 95px; top: 232px; width: 440px;
    text-align: center;
    font-size: 15px;
    line-height: 23px;
  }
  .method-title {
    position: absolute;
    left: 105px; top: 322px;
    font-size: 21px; font-weight: 700;
    letter-spacing: 4px;
    color: var(--charcoal);
  }
  .benefits {
    position: absolute;
    left: 32px; top: 360px;
    list-style: none;
    display: grid;
    grid-template-columns: 160px 260px;
    row-gap: 2px;
    font-size: 14.5px;
    line-height: 21px;
    white-space: nowrap;
  }
  .benefits li { display: flex; align-items: center; gap: 6px; }
  .benefits svg { width: 13px; height: 13px; flex: none; }
  .site-url {
    position: absolute;
    left: 50px; top: 420px;
    font-size: 17px; font-weight: 700;
    letter-spacing: 5.5px;
    color: var(--charcoal);
    white-space: nowrap;
  }

  /* Back */
  .question {
    position: absolute;
    left: 60px; top: 144px; width: 360px;
    text-align: center;
    font-size: 21px; font-weight: 700;
    color: var(--orange);
  }
  .points {
    position: absolute;
    left: 55px; top: 188px; width: 390px;
    list-style: none;
    font-size: 14px;
    line-height: 17px;
  }
  .points li {
    position: relative;
    padding-left: 38px;
    margin-bottom: 11px;
    text-align: justify;
  }
  .points li::before {
    content: "";
    position: absolute;
    left: 6px; top: 3px;
    width: 11px; height: 11px;
    background: var(--orange);
  }
  .proof {
    position: absolute;
    left: 472px; top: 170px; width: 155px;
    font-size: 19px; font-weight: 700;
    line-height: 30px;
    color: var(--orange);
  }
  .slogan {
    position: absolute;
    left: 0; top: 366px; width: 640px;
    text-align: center;
    font-size: 19px; font-weight: 700;
    letter-spacing: 2.4px;
    color: var(--orange);
    white-space: nowrap;
  }
  .contact {
    position: absolute;
    top: 410px;
    font-size: 13px;
    line-height: 21px;
    letter-spacing: 0.3px;
    white-space: nowrap;
  }
  .contact--left { left: 57px; }
  .contact--right { left: 405px; }
</style>
</head>
<body>

<section class="card card--front" aria-label="Rack card front">
  <svg class="card__stripes" viewBox="0 0 640 470" aria-hidden="true">
    <polygon points="0,0 95,0 0,380" fill="var(--orange)"/>
    <polygon points="95,0 138,0 0,470 0,380" fill="var(--charcoal)"/>
    <polygon points="138,0 190,0 20,470 0,470" fill="var(--light-grey)"/>
    <polygon points="190,0 225,0 45,470 20,470" fill="var(--pale-grey)"/>
    <polygon points="640,380 640,470 400,470" fill="var(--pale-grey)"/>
    <polygon points="640,230 640,470 520,470" fill="var(--light-grey)"/>
    <polygon points="640,200 640,470 555,470" fill="var(--charcoal)"/>
    <polygon points="640,195 640,470 585,470" fill="var(--orange)"/>
  </svg>

  <div class="brand"><span class="brand__mark"></span><span class="brand__name">THE FORMWELL</span></div>

  <div class="tagline-band">A safe and individualized approach to exercise</div>

  <p class="intro">Our method employs the latest weight resistance training<br>exer-cises and coaching for healthy living.<br>Not only is our workout methodology efective, it’s safe.</p>

  <h2 class="method-title">OUR METHOD</h2>

  <ul class="benefits">
    <li><svg viewBox="0 0 14 14"><path d="M1 7.5 L5 11.5 L13 2" fill="none" stroke="var(--orange)" stroke-width="2.6"/></svg>Builds Strength</li>
    <li><svg viewBox="0 0 14 14"><path d="M1 7.5 L5 11.5 L13 2" fill="none" stroke="var(--orange)" stroke-width="2.6"/></svg>Promotes Weight Loss</li>
    <li><svg viewBox="0 0 14 14"><path d="M1 7.5 L5 11.5 L13 2" fill="none" stroke="var(--orange)" stroke-width="2.6"/></svg>Increases Flexibility</li>
    <li><svg viewBox="0 0 14 14"><path d="M1 7.5 L5 11.5 L13 2" fill="none" stroke="var(--orange)" stroke-width="2.6"/></svg>Improves Functional Movement</li>
  </ul>

  <p class="site-url">www.corevantagestudio.com</p>
</section>

<section class="card card--back" aria-label="Rack card back">
  <svg class="card__stripes" viewBox="0 0 640 470" aria-hidden="true">
    <polygon points="0,190 640,60 640,75 0,250" fill="var(--pale-grey)" opacity="0.6"/>
    <polygon points="0,330 640,120 640,135 0,360" fill="var(--pale-grey)" opacity="0.5"/>
    <polygon points="330,0 640,0 640,290 450,0" fill="var(--pale-grey)"/>
    <polygon points="310,0 640,0 640,160" fill="var(--light-grey)"/>
    <polygon points="300,0 640,0 640,120" fill="var(--charcoal)"/>
    <polygon points="360,0 640,0 640,85" fill="var(--orange)"/>
  </svg>

  <div class="brand"><span class="brand__mark"></span><span class="brand__name">THE FORMWELL</span></div>

  <h2 class="question">What is The Formwell?</h2>

  <ul class="points">
    <li>The Formwell is all about teaching our clients how to lift weights and exercise with the proper technique.</li>
    <li>There’s no slinging or jerking at our gym; only controlled movements that yield real results.</li>
    <li>Come workout with us in our private gym. We are located in Durham adjacent to Harlow Campus and 5 minutes from downtown</li>
  </ul>

  <p class="proof">There’s<br>40 years of<br>success<br>behind<br>our proven<br>method</p>

  <p class="slogan">Change Your Body, Find Your Strength</p>

  <p class="contact contact--left">Address: 482 Linden Ave, Durham, NC 27705<br>Site: WWW.corevantagestudio.com</p>
  <p class="contact contact--right">Phone: (919) 555-2741<br>Hours: 9:00 AM – 9:00 PM</p>
</section>

</body>
</html>
```